GLENMARK VODKA LABELS DESIGN*

we Need a New label for Premium vodka "Glenmark Vodka" we are attaching design of current bottle and we need to change logo to Glenmark vodka with completely new design and concept . Please not that current logo is there just for example"

EXACT SIZE AND SHAPE OF LOGO ATTACHED

Logo Text

"glenmark vodka

```html
<!DOCTYPE html>
<html lang="sk">
<head>
<meta charset="utf-8">
<title>Velmoran Vodka – Label</title>
<link rel="stylesheet" href="https://fonts.googleapis.com/css2?family=Cinzel:wght@400;600;700&family=Playfair+Display:wght@700;900&family=Alegreya+Sans:wght@400&family=Libre+Caslon+Text&display=swap">
<style>
  :root {
    --page: #e9e5df;
    --label-black: #17171b;
    --label-black-edge: #0e0e11;
    --gold: #e2b94a;
    --gold-deep: #a87b22;
    --gold-light: #f6dc86;
    --brand-red: #b41c24;
    --band-red: #a4161d;
    --band-red-dark: #6f0c11;
    --ivory: #ece3cb;
  }
  * { margin: 0; padding: 0; box-sizing: border-box; }
  html, body {
    width: 800px;
    height: 1200px;
    overflow: hidden;
    background: var(--page);
  }
  .canvas {
    position: relative;
    width: 800px;
    height: 1200px;
  }
  .label {
    position: absolute;
    left: 95px;
    top: 55px;
    width: 610px;
    height: 1090px;
  }
  .label-small-caps {
    font-family: "Cinzel", serif;
    font-weight: 600;
    fill: var(--gold);
  }
  .label-brand {
    font-family: "Playfair Display", serif;
    font-weight: 900;
    fill: var(--brand-red);
  }
  .label-arc-line {
    font-family: "Cinzel", serif;
    font-weight: 700;
    fill: var(--gold);
    letter-spacing: 7px;
  }
  .label-category {
    font-family: "Playfair Display", serif;
    font-weight: 900;
    fill: var(--gold-light);
    letter-spacing: 3px;
  }
  .label-subtitle {
    font-family: "Cinzel", serif;
    font-weight: 400;
    fill: var(--ivory);
    letter-spacing: 3px;
  }
  .label-description {
    font-family: "Alegreya Sans", sans-serif;
    fill: var(--gold);
  }
  .label-volume {
    font-family: "Libre Caslon Text", serif;
    fill: var(--ivory);
  }
  .label-quality {
    font-family: "Cinzel", serif;
    font-weight: 700;
    fill: var(--gold);
    letter-spacing: 5px;
  }
  .gold-rule { stroke: var(--gold); stroke-width: 2; }
</style>
</head>
<body>
<main class="canvas">
  <svg class="label" viewBox="0 0 610 1090" xmlns="http://www.w3.org/2000/svg">
    <defs>
      <linearGradient id="label-body" x1="0" y1="0" x2="1" y2="0">
        <stop offset="0" stop-color="var(--label-black-edge)"/>
        <stop offset="0.5" stop-color="var(--label-black)"/>
        <stop offset="1" stop-color="var(--label-black-edge)"/>
      </linearGradient>
      <linearGradient id="band-fill" x1="0" y1="0" x2="0" y2="1">
        <stop offset="0" stop-color="var(--band-red)"/>
        <stop offset="1" stop-color="var(--band-red-dark)"/>
      </linearGradient>
      <radialGradient id="seal-fill" cx="0.5" cy="0.5" r="0.5">
        <stop offset="0" stop-color="var(--gold-light)"/>
        <stop offset="1" stop-color="var(--gold-deep)"/>
      </radialGradient>
      <radialGradient id="seal-glow" cx="0.5" cy="0.5" r="0.5">
        <stop offset="0" stop-color="var(--gold)" stop-opacity="0.35"/>
        <stop offset="1" stop-color="var(--gold)" stop-opacity="0"/>
      </radialGradient>
      <path id="arc-extra" d="M120,488 Q305,575 490,488"/>
    </defs>

    <!-- label shape and frame -->
    <path class="label-shape" fill="url(#label-body)"
      d="M0,150 A28,28 0 0 0 28,122 Q305,-100 582,122 A28,28 0 0 0 610,150 L610,1050 A40,40 0 0 0 570,1090 L40,1090 A40,40 0 0 0 0,1050 Z"/>
    <path class="label-frame" fill="none" stroke="var(--gold)" stroke-width="3"
      d="M14,152 A22,22 0 0 0 36,130 Q305,-78 574,130 A22,22 0 0 0 596,152 L596,1046 A34,34 0 0 0 562,1076 L48,1076 A34,34 0 0 0 14,1046 Z"/>

    <!-- distillery seal area -->
    <circle cx="305" cy="150" r="105" fill="url(#seal-glow)"/>
    <circle class="label-seal" cx="305" cy="150" r="60" fill="url(#seal-fill)"
      role="img" aria-label="Distillery seal emblem"/>

    <!-- heritage line -->
    <text class="label-small-caps" x="150" y="318" font-size="24" text-anchor="middle" letter-spacing="4" transform="rotate(-8 150 318)">ANNO</text>
    <text class="label-small-caps" x="460" y="318" font-size="24" text-anchor="middle" letter-spacing="4" transform="rotate(8 460 318)">1867</text>

    <!-- brand name -->
    <text class="label-brand" x="305" y="448" font-size="96" text-anchor="middle" textLength="530" lengthAdjust="spacingAndGlyphs">VELMORAN</text>

    <!-- arched tagline -->
    <text class="label-arc-line" font-size="34">
      <textPath href="#arc-extra" startOffset="50%" text-anchor="middle">EXTRA LEMNA</textPath>
    </text>

    <!-- category band -->
    <rect x="14" y="585" width="582" height="100" fill="url(#band-fill)"/>
    <line class="gold-rule" x1="14" y1="585" x2="596" y2="585"/>
    <line class="gold-rule" x1="14" y1="685" x2="596" y2="685"/>
    <text class="label-category" x="305" y="660" font-size="64" text-anchor="middle">VODKA</text>

    <!-- filtration subtitle -->
    <line class="gold-rule" x1="14" y1="708" x2="596" y2="708"/>
    <line class="gold-rule" x1="30" y1="738" x2="580" y2="738"/>
    <text class="label-subtitle" x="305" y="782" font-size="29" text-anchor="middle">STRIEBROM FILTROVANA</text>
    <line class="gold-rule" x1="30" y1="806" x2="580" y2="806"/>

    <!-- description -->
    <text class="label-description" font-size="20" text-anchor="middle">
      <tspan x="305" y="868">Filtracia cez 24 specialnych filtrov z aktivneha</tspan>
      <tspan x="305" y="898">striebra a kristalove cista tatranska voda, dava</tspan>
      <tspan x="305" y="928">nasy vodke Extra jemnii chut a vonu</tspan>
    </text>

    <!-- volume and strength -->
    <text class="label-volume" x="30" y="1002" font-size="18">1000 ml</text>
    <text class="label-volume" x="580" y="1002" font-size="18" text-anchor="end">38% obj</text>

    <!-- quality line -->
    <text class="label-quality" x="305" y="1046" font-size="20" text-anchor="middle">EXTRA FINE QUALITY</text>
  </svg>
</main>
</body>
</html>
```